Luxury Inclusive Beauty Brand Needs Labels & Boxes for Product Line

We need updated labels and boxes for our cosmetic and skin care line. Our company is MAVRA & CO. and we focus on providing upscale, natural and organic beauty products inclusive of diverse and deeper skin tones for women of color, especially black women. We have a seven piece skin care collection called DERMAVELLE Baobin Collection and a mineral make-up line consisting of eight products. The design of all products should be the same with just dimensions and title/ingredient list differences. We would like to see designs that use our coral color e85350, work well on black packaging (bottles, lipstick tubes etc.) and include white and other additional pretty colors, metallics or patterns representative of ethnic (AFRICAN), bohemian or tribal influence. The final design should communicate luxury, floral/fauna environmentalism, and afrocentric culture influences.
We have included files of various prints we like and the type of lifestyle our customer aspires to/is attracted to. We have included in the files below some examples of packaging we like but we want something original to capture the attention of our target market, upper income health and ethnic conscious black women age 30 - 55 who love natural and organic products. The names of our products include the list below however if design can be submitted showing design on 1 tall box and 1 short box and 1 lipstick size box that would be great:
DERMAVELLE Baobin Collection Cleansing Oil (dropper)
DERMAVELLE Baobin Collection Balancing Toner (tall spray bottle)
DERMAVELLE Baobin Collection Moisturizing Serum (dropper)
DERMAVELLE Baobin Collection Moisturizing Cream (short box jar)
DERMAVELLE Baobin Lip Scrub (short box - jar)
Luminous Mineral Foundation (short box- jar)
CC Cream
Moisturizing Lip Stick (lipstick box)
OTIRAFLIX Natural Mascara
Zarra Bimble Lip Crayon
Gel Eye Liner
Organic Make-up Remover (tall spray bottle)
Face & Eye Primer
Final dimensions /dies of boxes can be sent to winner of design competition.
Target Market(s)
women of color, age 30-55, income 50 - 150K, natural hair and organic lifestyle, yoga
Industry/Entity Type
Cosmetics
Requirements
Must have
- label and box
- include the color e85350
- include logo
Nice to have
- easy way to differentiate skincare from make-up products

```html
<!DOCTYPE html>
<html lang="en">
<head>
<meta charset="utf-8">
<title>MAVRA &amp; CO. — Baobin Collection Packaging</title>
<link href="https://fonts.googleapis.com/css2?family=Josefin+Sans:wght@100;300&display=swap" rel="stylesheet">
<style>
  :root {
    --bg: #ffffff;
    --red: #d9263a;
    --coral: #e85350;
    --magenta: #a3308f;
    --purple: #5b35a0;
    --indigo: #3b3f9c;
    --teal: #0aa89e;
    --jar-black: #2c2c2e;
    --white: #ffffff;
    --pattern-gradient: linear-gradient(135deg, #e0343f 0%, #2aa69c 25%, #6a3aa6 50%, #d42f55 75%, #1aa89c 100%);
    --panel-gradient: linear-gradient(180deg, var(--red) 0%, var(--magenta) 38%, var(--purple) 58%, var(--indigo) 72%, var(--teal) 100%);
  }
  * { box-sizing: border-box; margin: 0; padding: 0; }
  html, body { width: 1200px; height: 1029px; overflow: hidden; background: var(--bg); }
  body { position: relative; font-family: 'Josefin Sans', sans-serif; font-weight: 300; color: var(--white); }

  .pack { position: absolute; }
  .pattern { position: absolute; inset: 0; background: var(--pattern-gradient); }

  .label-panel {
    position: absolute;
    background: var(--panel-gradient);
    display: flex; flex-direction: column; align-items: center;
    text-align: center; text-transform: uppercase;
    padding-top: 1.1em;
  }
  .brand { display: flex; flex-direction: column; align-items: center; font-size: 0.85em; letter-spacing: 0.02em; }
  .brand-dot { width: 1.3em; height: 1.3em; border: 1px solid var(--white); border-radius: 50%; margin-bottom: 0.25em; }
  .initial { font-weight: 100; font-size: 8.2em; line-height: 0.78; margin-top: 0.08em; }
  .line-name { font-size: 1.25em; line-height: 1.05; }
  .line-collection { font-size: 0.95em; line-height: 1.15; }
  .product { font-size: 1.15em; margin-top: auto; letter-spacing: 0.02em; }
  .tagline { font-size: 0.7em; margin-top: 1.5em; margin-bottom: 2.6em; letter-spacing: 0.03em; }

  /* Cream label (flat) */
  .cream-label { left: 478px; top: 213px; width: 238px; height: 307px; }
  .cream-label .label-panel { inset: 0; font-size: 15px; padding-top: 1em; }

  /* Tall toner box */
  .toner-box { left: 834px; top: 86px; width: 278px; height: 558px; }
  .toner-box .label-panel { left: 68px; top: 71px; width: 143px; height: 414px; font-size: 17px; }
  .toner-box .initial { font-size: 7.6em; }
  .toner-box .product { font-size: 0.75em; margin-top: 2.2em; }
  .toner-box .tagline { font-size: 0.48em; margin-top: auto; margin-bottom: 3.5em; }

  /* Toner bottle label */
  .toner-label { left: 98px; top: 453px; width: 178px; height: 353px; }
  .toner-label .label-panel { left: 43px; top: 45px; width: 91px; height: 262px; font-size: 10.5px; }
  .toner-label .initial { font-size: 7.6em; }
  .toner-label .product { font-size: 0.68em; margin-top: 2.2em; }
  .toner-label .tagline { font-size: 0.45em; margin-top: auto; margin-bottom: 3.5em; }

  /* Serum label */
  .serum-label { left: 325px; top: 718px; width: 58px; height: 165px; }
  .serum-label .label-panel { left: 4px; top: 24px; width: 50px; height: 118px; font-size: 5.6px; }
  .serum-label .initial { font-size: 7.4em; }
  .serum-label .product { font-size: 0.6em; margin-top: 2.2em; }
  .serum-label .tagline { font-size: 0.5em; margin-top: auto; margin-bottom: 2.5em; }

  /* Wide cream box */
  .cream-box { left: 420px; top: 654px; width: 350px; height: 274px; }
  .cream-box .label-panel { left: 96px; top: 35px; width: 158px; height: 202px; font-size: 10px; padding-top: 0.9em; }
  .cream-box .tagline { margin-bottom: 2.4em; }

  /* Black jar labels */
  .jar-label {
    background: var(--jar-black); display: flex; align-items: center; gap: 0.9em;
    text-transform: uppercase; padding-left: 3.4em;
  }
  .jar-mark { display: flex; flex-direction: column; align-items: center; text-align: center; }
  .jar-mark .initial { font-size: 6.4em; }
  .jar-text { align-self: flex-start; margin-top: 4.2em; }
  .jar-text .product { font-size: 1.15em; margin: 0; }
  .jar-text .tagline { font-size: 0.7em; margin: 1.3em 0 0; }
  .cream-jar { left: 700px; top: 764px; width: 198px; height: 156px; font-size: 10px; }
  .eye-jar { left: 906px; top: 810px; width: 170px; height: 118px; font-size: 7.5px; padding-left: 2.4em; }
  .eye-jar .jar-text { margin-top: 5em; }
  .eye-jar .tagline { font-size: 0.75em; line-height: 1.3; }
</style>
</head>
<body>

  <section class="pack toner-label" aria-label="Balancing toner bottle label">
    <div class="pattern" role="img" aria-label="Ornate red, teal and violet mandala pattern"></div>
    <div class="label-panel">
      <div class="brand"><span class="brand-dot"></span>MAVRA &amp; CO.</div>
      <div class="initial">B</div>
      <div class="line-name">Baobin</div>
      <div class="line-collection">Collection</div>
      <div class="product">Balancing Toner</div>
      <div class="tagline">Refines &amp; Minimizes Pores</div>
    </div>
  </section>

  <section class="pack serum-label" aria-label="Serum dropper label">
    <div class="pattern" role="img" aria-label="Ornate red, teal and violet mandala pattern"></div>
    <div class="label-panel">
      <div class="brand"><span class="brand-dot"></span>MAVRA &amp; CO.</div>
      <div class="initial">B</div>
      <div class="line-name">Baobin</div>
      <div class="line-collection">Collection</div>
      <div class="product">Renewing Serum</div>
      <div class="tagline">Glow &amp; Protect</div>
    </div>
  </section>

  <section class="pack cream-label" aria-label="Moisturising cream label">
    <div class="label-panel">
      <div class="brand"><span class="brand-dot"></span>MAVRA &amp; CO.</div>
      <div class="initial">B</div>
      <div class="line-name">Baobin</div>
      <div class="line-collection">Collection</div>
      <div class="product">Moisturising Cream</div>
      <div class="tagline">Revitalising and Firming</div>
    </div>
  </section>

  <section class="pack toner-box" aria-label="Balancing toner tall box">
    <div class="pattern" role="img" aria-label="Ornate red, teal and violet mandala pattern"></div>
    <div class="label-panel">
      <div class="brand"><span class="brand-dot"></span>MAVRA &amp; CO.</div>
      <div class="initial">B</div>
      <div class="line-name">Baobin</div>
      <div class="line-collection">Collection</div>
      <div class="product">Balancing Toner</div>
      <div class="tagline">Refines &amp; Minimizes Pores</div>
    </div>
  </section>

  <section class="pack cream-box" aria-label="Moisturising cream short box">
    <div class="pattern" role="img" aria-label="Ornate red, teal and violet mandala pattern"></div>
    <div class="label-panel">
      <div class="brand"><span class="brand-dot"></span>MAVRA &amp; CO.</div>
      <div class="initial">B</div>
      <div class="line-name">Baobin</div>
      <div class="line-collection">Collection</div>
      <div class="product">Moisturising Cream</div>
      <div class="tagline">Revitalising and Firming</div>
    </div>
  </section>

  <section class="pack jar-label cream-jar" aria-label="Moisturising cream jar label">
    <div class="jar-mark">
      <div class="brand"><span class="brand-dot"></span>MAVRA &amp; CO.</div>
      <div class="initial">B</div>
      <div class="line-name">Baobin</div>
      <div class="line-collection">Collection</div>
    </div>
    <div class="jar-text">
      <div class="product">Moisturising Cream</div>
      <div class="tagline">Revitalising and Firming</div>
    </div>
  </section>

  <section class="pack jar-label eye-jar" aria-label="Eye contour care jar label">
    <div class="jar-mark">
      <div class="brand"><span class="brand-dot"></span>MAVRA &amp; CO.</div>
      <div class="initial">B</div>
      <div class="line-name">Baobin</div>
      <div class="line-collection">Collection</div>
    </div>
    <div class="jar-text">
      <div class="product">Eye Contour Care</div>
      <div class="tagline">Anti-Wrinkle and<br>Anti-Dark Circles</div>
    </div>
  </section>

</body>
</html>
```